Wix Website

I would like to migrate my current website (www.meadowlarkprep.com) over to a Wix template. Right now, I think my site is too playful. I am looking for a really clean, modern and updated feel. I still want a classical feel. Simple the better. As for what we do, we are a provider of in-home tutoring. We service young to old. students alike. Looking for something academic but not pre-school. A good balance of elementary to high school.

Looking also to scale down the site to as little pages as possible. Again, simple the better. Would like a really good home page and an even better landing page that highlights a quick and easy signup form.

Please feel free to get as much info off the current site to make the page. The final design should highlight "The Human Side of Tutoring". Please make sure our tagline of "Helping students and their parents live above the stress and strain of academic struggles" is prominent. Appropriate Stock photos are permissible at this time. We can change them as needed

```html
<!DOCTYPE html>
<html lang="en">
<head>
<meta charset="utf-8">
<title>Meadowlark Prep – In-Home Tutoring</title>
<link href="https://fonts.googleapis.com/css2?family=Roboto:wght@300;400;500;700&family=Roboto+Condensed:wght@700&display=swap" rel="stylesheet">
<style>
:root{
  --header-brown:#4a423d;
  --orange:#e0782f;
  --orange-dark:#c9662a;
  --red:#d7203f;
  --quote-red:#e0603a;
  --brand-red:#c92a2a;
  --grey-bar:#4b4b4b;
  --grey-bar-dark:#3b3b3b;
  --panel:#f6f6f6;
  --text:#555;
  --muted:#8a8a8a;
  --gold:#f6b320;
  --footer:#0b0b0b;
  --white:#fff;
}
*{box-sizing:border-box;margin:0;padding:0}
html,body{width:1056px;height:1200px;overflow:hidden;background:var(--white)}
body{position:relative;font-family:'Roboto',sans-serif;color:var(--text)}
.abs{position:absolute}

/* header */
.topbar{left:0;top:0;width:1056px;height:94px;background:var(--header-brown)}
.top-links{right:150px;top:18px;display:flex;gap:34px;color:var(--white);font-size:14px}
.call{right:150px;top:55px;color:var(--white);font-size:14px}
.mainnav{left:0;top:94px;width:1056px;height:42px;background:var(--orange)}
.mainnav ul{position:absolute;left:350px;top:0;display:flex;list-style:none;height:42px}
.mainnav li{color:var(--white);font-size:14px;line-height:42px;padding:0 18px;border-left:1px solid var(--orange-dark)}
.mainnav li:first-child{border-left:none}
.brand{left:151px;top:0;width:193px;height:137px;background:var(--white);
  clip-path:polygon(0 0,100% 0,100% 82%,50% 100%,0 82%);
  display:flex;align-items:center;justify-content:center;gap:8px;padding-bottom:22px}
.brand-dot{width:14px;height:14px;border-radius:50%;background:var(--orange)}
.brand-name{font-size:20px;font-weight:700;color:var(--brand-red)}

/* hero */
.hero{left:0;top:136px;width:1056px;height:450px;
  background:linear-gradient(90deg,#6b4a2c 0%,#b98756 30%,#a26a3a 55%,#7a4f2c 80%,#5a3a22 100%)}
.arrow{width:30px;height:30px;border-radius:50%;background:rgba(60,50,45,.75);top:333px}
.tagline-box{left:154px;top:446px;width:462px;height:114px;background:rgba(60,55,52,.72);padding:10px 0 0 30px}
.tagline{font-family:'Roboto Condensed',sans-serif;font-weight:700;font-size:27px;line-height:32px;color:var(--white)}

.quote-form{left:616px;top:196px;width:289px;height:390px;background:rgba(85,70,60,.82)}
.quote-head{height:40px;background:var(--quote-red);color:var(--white);font-size:18px;line-height:40px;padding-left:16px}
.field{position:absolute;font-size:11px;color:#eee}
.field span{display:block;margin-bottom:10px}
.field i{display:block;width:126px;height:31px;background:var(--white);border-radius:2px}
.field.wide i{width:263px}
.signup{left:78px;top:338px;width:131px;height:36px;background:var(--red);color:var(--white);font-size:16px;text-align:center;line-height:36px;border-radius:2px}

/* announcement */
.announce{left:0;top:586px;width:1056px;height:53px;background:var(--grey-bar)}
.announce-label{left:151px;top:0;color:var(--white);font-size:19px;font-weight:300;line-height:53px}
.announce-text{left:299px;top:0;width:556px;height:53px;background:#555;color:var(--white);font-size:11px;line-height:53px;padding-left:30px}
.announce-ctrl{left:855px;top:0;width:51px;height:53px;background:var(--grey-bar-dark);display:flex;justify-content:space-around;align-items:center}

/* features */
.feature{top:696px;width:236px;height:128px;background:var(--panel);text-align:center;padding-top:38px}
.feature h3{font-size:16px;font-weight:400;color:var(--orange-dark);margin-bottom:8px}
.feature p{font-size:10px;line-height:17.5px;color:var(--muted);padding:0 12px;font-weight:300}
.feature-icon{width:60px;height:60px;border-radius:50%;top:668px}

/* welcome */
.welcome-title{left:151px;top:852px;font-size:23px;font-weight:400;color:#555}
.welcome-title em{font-style:normal;color:var(--brand-red)}
.welcome-photo{left:151px;top:898px;width:236px;height:180px;background:linear-gradient(135deg,#e6e8ea,#c9ccd0 60%,#8fb7c9)}
.welcome-copy{left:409px;top:894px;width:237px}
.welcome-copy h4{font-size:16px;font-weight:300;line-height:23px;color:#444;margin-bottom:12px}
.welcome-copy p{font-size:10.5px;line-height:19px;color:var(--muted);text-align:justify;font-weight:300}
.welcome-copy a{display:block;margin-top:10px;font-size:11px;color:#555;text-decoration:none}

.testi-title{left:669px;top:856px;font-size:17px;color:var(--orange-dark)}
.testi-box{left:669px;top:900px;width:237px;height:152px;background:var(--panel);padding:40px 18px 0 19px;clip-path:polygon(0 0,100% 0,100% 100%,95% 100%,92% 108%,0 100%)}
.testi-box p{font-size:9.5px;line-height:19px;color:var(--muted);text-align:justify}
.dots{right:16px;top:12px;display:flex;gap:4px}
.dots i{width:6px;height:6px;border-radius:50%;background:#ddd}
.dots i.on{background:var(--orange)}
.qmark{font-family:Georgia,serif;font-size:26px;color:#aaa}
.testi-name{left:828px;top:1064px;font-size:11px;font-style:italic;color:var(--orange-dark)}

/* footer */
.footer{left:0;top:1124px;width:1056px;height:76px;background:var(--footer);color:#ccc}
.copy{left:151px;top:16px;font-size:11px}
.foot-links{left:151px;top:46px;font-size:9.5px;color:#bbb}
.social{left:543px;top:26px;display:flex;gap:6px}
.social i{width:24px;height:24px;border-radius:50%;border:1px solid #555}
.addr{right:149px;top:18px;font-size:10px;text-align:right}
.phone{right:149px;top:42px;font-size:14px}
</style>
</head>
<body>

<header>
  <div class="abs topbar"></div>
  <nav class="abs top-links"><span>What</span><span>Why</span><span>Who</span><span>How</span><span>Let's Go!</span></nav>
  <div class="abs call">Call Us : 555 - 014 - 2290</div>
  <nav class="abs mainnav"><ul><li>Home</li><li>Our Story</li><li>Our Tutoring</li><li>FAQ</li><li>Summer Tutoring</li><li>Contact</li></ul></nav>
  <div class="abs brand"><span class="brand-dot"></span><span class="brand-name">Meadowlark Prep</span></div>
</header>

<section>
  <div class="abs hero" role="img" aria-label="Photo of a student reading a tablet in a library with bookshelves behind"></div>
  <div class="abs arrow" style="left:34px"><svg width="30" height="30"><path d="M17 9l-6 6 6 6" stroke="#fff" stroke-width="2" fill="none"/></svg></div>
  <div class="abs arrow" style="left:992px"><svg width="30" height="30"><path d="M13 9l6 6-6 6" stroke="#fff" stroke-width="2" fill="none"/></svg></div>
  <div class="abs tagline-box"><h1 class="tagline">Helping students and their parents live above the stress and strain of academic struggles</h1></div>

  <form class="abs quote-form">
    <div class="quote-head">Get a Free Quote</div>
    <label class="field" style="left:16px;top:60px"><span>First Name *</span><i></i></label>
    <label class="field" style="left:152px;top:60px"><span>Student's Grade *</span><i></i></label>
    <label class="field" style="left:16px;top:128px"><span>Email *</span><i></i></label>
    <label class="field" style="left:152px;top:128px"><span>Phone Number *</span><i></i></label>
    <label class="field" style="left:16px;top:196px"><span>State *</span><i></i></label>
    <svg class="abs" style="left:120px;top:232px" width="12" height="8"><path d="M0 0h11L5.5 7z" fill="#999"/></svg>
    <label class="field" style="left:152px;top:196px"><span>Zip *</span><i></i></label>
    <label class="field wide" style="left:16px;top:264px"><span>Please describe your needs*</span><i></i></label>
    <div class="abs signup">Signup Now</div>
  </form>
</section>

<section class="abs announce">
  <div class="abs announce-label">Announcement</div>
  <div class="abs announce-text">Summer vacation is among the most pernicious, if least acknowledged, causes of achievement gaps</div>
  <div class="abs announce-ctrl">
    <svg width="8" height="10"><path d="M6 1L2 5l4 4" stroke="#fff" stroke-width="1.5" fill="none"/></svg>
    <svg width="8" height="10"><path d="M2 1l4 4-4 4" stroke="#fff" stroke-width="1.5" fill="none"/></svg>
  </div>
</section>

<section>
  <div class="abs feature" style="left:151px"><h3>GET HELP</h3><p>Is your child struggling in school and needs help that you can't provide? In home tutoring from Meadowlark Prep provides the opportunity</p></div>
  <div class="abs feature" style="left:410px"><h3>GET BACK ON TRACK</h3><p>Getting back on track is easy when your struggling student is matched with the ideal tutor that meets their needs. Our tutors are</p></div>
  <div class="abs feature" style="left:669px"><h3>GET RESULTS</h3><p>Through the assistance tutoring provides, your child will get results. You will see not only academic improvements, but aslo increased</p></div>

  <div class="abs feature-icon" style="left:239px;background:var(--gold)"><svg width="60" height="60"><path d="M30 38c-7-5-11-9-11-13a5 5 0 0 1 11-2 5 5 0 0 1 11 2c0 4-4 8-11 13z" fill="#fff"/></svg></div>
  <div class="abs feature-icon" style="left:491px;background:#f57d1f"><svg width="60" height="60" fill="none" stroke="#fff" stroke-width="4"><path d="M19 28a11 11 0 0 1 20-5"/><path d="M41 32a11 11 0 0 1-20 5"/><path d="M36 19l4 4-5 2" stroke-width="3"/><path d="M24 41l-4-4 5-2" stroke-width="3"/></svg></div>
  <div class="abs feature-icon" style="left:758px;background:var(--orange-dark)"><svg width="60" height="60" fill="#fff"><rect x="16" y="28" width="6" height="15"/><path d="M24 28l6-10c2-1 4 0 4 3l-1 6h8c2 0 3 2 3 3l-3 11c-1 2-2 2-3 2H24z"/></svg></div>
</section>

<section>
  <h2 class="abs welcome-title">Welcome To <em>Meadowlark Prep</em></h2>
  <div class="abs welcome-photo" role="img" aria-label="Photo of a smiling student raising her hand and holding folders"></div>
  <div class="abs welcome-copy">
    <h4>Helping students and their parents live above the stress</h4>
    <p>We are educators. Yes, educators to the core. Helen is a certified English teacher and Marcus, an administrator (in fact, a retired high school principal). We both love teaching and love learning. We have had the honor and privilege of working at some of the best schools around.</p>
    <a href="#">Read More</a>
  </div>

  <h2 class="abs testi-title">Testimonials</h2>
  <div class="abs testi-box">
    <div class="abs dots"><i></i><i></i><i></i><i class="on"></i></div>
    <span class="abs qmark" style="left:12px;top:10px">“</span>
    <p>Lorem ipsum dolor sit amet, consectetur adipiscing elit, sed do eiusmod tempor incididunt ut labore et dolore magna aliqua. Ut enim ad minim veniam, quis nostrud exercitation ullamco laboris nisi ut</p>
    <span class="abs qmark" style="right:16px;top:112px">”</span>
  </div>
  <div class="abs testi-name">John Doe</div>
</section>

<footer class="abs footer">
  <div class="abs copy">©2014 Meadowlark Prep , All Rights Reserved.</div>
  <div class="abs foot-links">Home &nbsp;| &nbsp;Our Tutoring &nbsp;| &nbsp;Our Story &nbsp;| &nbsp;Areas We Serve &nbsp;| &nbsp;Contact</div>
  <div class="abs social"><i></i><i></i><i></i></div>
  <div class="abs addr">12 Meadowlark Lane, London</div>
  <div class="abs phone">Phone: +1.555.014.2290</div>
</footer>

</body>
</html>
```